Bedrock Yield Private Holdings Scheme

I want a professional design for a new investment program that we have designed for prospecting new prospects. We have a company logo and the content that we would like for the brochure but we would like and design structure and graphics to help compliment the content. I am attaching a rough draft of the brochure that has some

Target Market(s)

Anyone looking for hard assets, inflation hedge, cash flow investments.

```html
<!DOCTYPE html>
<html lang="en">
<head>
<meta charset="utf-8">
<title>Bedrock Yield Private Holdings Scheme – Brochure Spreads</title>
<link href="https://fonts.googleapis.com/css2?family=Poppins:wght@300;400;500;600;700&display=swap" rel="stylesheet">
<style>
  :root{
    --backdrop:#93b098;
    --backdrop-light:#b9cdbc;
    --green:#2f5e3a;
    --green-bright:#2f8a45;
    --gold:#d9a232;
    --paper:#f8f8f8;
    --grey:#e4e4e4;
    --grey-mid:#cfcfcf;
    --ink:#4f4f4f;
    --white:#fff;
  }
  *{box-sizing:border-box;margin:0;padding:0}
  html,body{width:876px;height:1200px;overflow:hidden}
  body{position:relative;background:var(--backdrop);font-family:"Poppins",sans-serif;color:var(--ink)}
  .backdrop-diagonal{position:absolute;inset:0}
  .page{position:absolute;width:372px;height:526px;background:var(--paper);overflow:hidden;box-shadow:0 3px 8px rgba(0,0,0,.18)}
  .page svg.page-art{position:absolute;inset:0}
  .cover{left:46px;top:55px}
  .about{left:454px;top:60px}
  .process{left:46px;top:614px}
  .contact{left:454px;top:614px}

  .footer-band{position:absolute;left:0;right:0;bottom:0;height:17px;background:var(--gold);color:var(--white);
    font-size:9px;font-weight:600;letter-spacing:2.6px;text-align:center;line-height:17px}
  .page-tab{position:absolute;bottom:0;width:24px;height:24px;background:var(--gold);color:var(--white);
    font-size:8px;font-weight:500;text-align:center;line-height:26px;
    clip-path:polygon(50% 0,100% 25%,100% 100%,0 100%,0 25%)}

  .brand-name{position:absolute;color:var(--green);font-weight:600;text-align:center;line-height:1.1;text-transform:uppercase}
  .cover .brand-name{left:6px;top:40px;width:86px;font-size:10.5px}
  .cover-title{position:absolute;left:123px;top:42px;width:249px;text-align:center;color:var(--white);
    font-weight:700;font-size:31px;line-height:41px;letter-spacing:.3px}

  .section-head{position:absolute;height:26px}
  .section-head svg{position:absolute;left:0;top:-6px;width:52px;height:36px;z-index:2}
  .section-head .pill{position:absolute;left:32px;top:2px;height:22px;background:var(--green);color:var(--white);
    font-weight:700;font-size:10.5px;line-height:22px;padding:0 10px 0 22px;border-radius:0 11px 11px 0;white-space:nowrap}

  .body-copy{position:absolute;font-size:8.6px;font-weight:300;line-height:10.45px;text-align:justify;color:var(--ink)}

  .framed-photo{position:absolute;border:2px solid var(--gold);background:var(--white);padding:5px}
  .framed-photo .fill{width:100%;height:100%}

  .step-label{position:absolute;text-align:center;color:#333;width:70px;margin-left:-35px}
  .step-label b{display:block;font-size:12px;font-weight:600;line-height:13px;border-bottom:1px solid #333;width:17px;margin:0 auto 1px}
  .step-label span{display:block;font-size:6px;font-weight:500;letter-spacing:.2px;line-height:8px}

  .why-copy{position:absolute;left:26px;top:340px;width:316px}
  .why-copy .framed-photo{position:static;float:right;width:133px;height:100px;margin:2px 0 6px 12px}
  .bullet-list{list-style:none}
  .bullet-list li{font-size:8.6px;font-weight:300;line-height:10.45px;text-align:justify;color:var(--ink);margin-bottom:5px}

  .contact-list{position:absolute;left:112px;top:270px;width:180px;list-style:none;color:var(--white)}
  .contact-list li{display:flex;align-items:flex-start;gap:8px;font-weight:600}
  .contact-list svg{flex:none;width:16px;height:16px}
  .contact .brand-name{left:136px;top:226px;width:100px;color:var(--white);font-size:10px}
</style>
</head>
<body>

<svg class="backdrop-diagonal" width="876" height="1200" aria-hidden="true">
  <polygon points="876,600 876,1200 300,1200" fill="var(--backdrop-light)"/>
</svg>

<!-- Cover -->
<section class="page cover">
  <svg class="page-art" viewBox="0 0 372 526" aria-hidden="true">
    <polygon points="0,180 85,130 85,175 0,225" fill="var(--grey)"/>
    <polygon points="85,95 123,75 123,215 250,288 372,220 372,260 250,330 85,240" fill="var(--grey-mid)"/>
    <polygon points="120,300 200,255 290,305 290,340 200,290 120,335" fill="var(--grey)" opacity=".7"/>
    <path d="M123,78 L85,100 L85,240" fill="none" stroke="var(--green)" stroke-width="9"/>
    <path d="M164,300 L205,323 Q215,329 226,323 L355,250 Q363,245 363,235 L363,205" fill="none" stroke="var(--green)" stroke-width="9"/>
    <defs>
      <linearGradient id="coinsGold" x1="0" y1="0" x2="1" y2="1">
        <stop offset="0" stop-color="#c98f2e"/><stop offset=".5" stop-color="#e0a842"/><stop offset="1" stop-color="#b07a26"/>
      </linearGradient>
      <linearGradient id="sproutGreen" x1="0" y1="0" x2="0" y2="1">
        <stop offset="0" stop-color="#7fae3c"/><stop offset=".6" stop-color="#5d8a2e"/><stop offset="1" stop-color="#b89a6a"/>
      </linearGradient>
      <linearGradient id="marketBlue" x1="0" y1="0" x2="1" y2="1">
        <stop offset="0" stop-color="#e2a18c"/><stop offset=".35" stop-color="#4d6fb6"/><stop offset="1" stop-color="#1f4fa8"/>
      </linearGradient>
    </defs>
    <polygon role="img" aria-label="Close-up photo of gold coins" points="123,0 372,0 372,215 250,283 123,215" fill="url(#coinsGold)"/>
    <polygon role="img" aria-label="Photo of seedlings growing from stacks of coins" points="90,234 166,278 166,366 90,410 14,366 14,278" fill="url(#sproutGreen)" stroke="var(--green)" stroke-width="9" stroke-linejoin="round"/>
    <polygon role="img" aria-label="Photo of blue coin stacks in front of a stock chart" points="290,311 377,361 377,461 290,511 203,461 203,361" fill="url(#marketBlue)" stroke="var(--grey)" stroke-width="6" stroke-linejoin="round"/>
  </svg>
  <div class="brand-name">Stonebrook<br>Minerals, LLC</div>
  <h1 class="cover-title">PRIVATE<br>HOLDINGS<br>SCHEME<br>2021</h1>
  <div class="footer-band">www.website.com</div>
</section>

<!-- About page -->
<section class="page about">
  <svg class="page-art" viewBox="0 0 372 526" aria-hidden="true">
    <g fill="none" stroke="#ececec" stroke-width="10">
      <polygon points="190,40 280,-10 372,40 372,140 280,190 190,140"/>
      <polygon points="0,300 60,265 120,300 120,380 60,415 0,380"/>
    </g>
  </svg>
  <header class="section-head" style="left:10px;top:24px">
    <svg viewBox="0 0 52 36" aria-hidden="true">
      <polygon points="10,11 18,15.5 18,24.5 10,29 2,24.5 2,15.5" fill="#cfcfcf"/>
      <polygon points="20,1 25,4 25,9 20,12 15,9 15,4" fill="var(--gold)"/>
      <polygon points="34,4 48,12 48,28 34,36 20,28 20,12" fill="var(--green)"/>
    </svg>
    <h2 class="pill">WHO WE ARE?</h2>
  </header>
  <p class="body-copy" style="left:32px;top:67px;width:310px">What should investors do to in this uncertain period to profit from the evolving energy transition and protect themselves from what appears to be an inevitable wave of inflation? We have one asset class and a business opportunity behind it that can address both.</p>
  <figure class="framed-photo" style="left:49px;top:134px;width:281px;height:197px">
    <div class="fill" role="img" aria-label="Black and white photo of a newspaper investment page with signposts and glasses" style="background:linear-gradient(135deg,#3a3a3a,#9a9a9a 45%,#d8d8d8 70%,#6a6a6a)"></div>
  </figure>
  <p class="body-copy" style="left:32px;top:345px;width:310px">Stonebrook Minerals is a successful oil and gas mineral/royalty firm whose business model is to identify, acquire, manage, and divest energy royalty assets. Located in Cedar Falls, Texas, Stonebrook’s focus in the last 11 years has been on acquiring producing domestic energy royalty interests for our various partnerships, family offices, and individuals. Through years of hard work, we have developed the infrastructure to create outstanding royalty portfolios for these groups but have now adapted that to accommodate individuals outside of these structures. With the scale we have developed, we can manage the transactions inexpensively throughout the entire process and cut out middlemen and brokers who dilute investor returns. Basically, buy these legacy assets and transition them to investors at relatively the same price as industry buyers have for years.</p>
  <div class="footer-band" style="left:26px"></div>
  <div class="page-tab" style="left:0">2</div>
</section>

<!-- Process page -->
<section class="page process">
  <svg class="page-art" viewBox="0 0 372 526" aria-hidden="true">
    <g fill="none" stroke="#eeeeee" stroke-width="10">
      <polygon points="260,60 330,20 400,60 400,140 330,180 260,140"/>
      <polygon points="-20,300 40,265 100,300 100,380 40,415 -20,380"/>
    </g>
    <g fill="none" stroke="var(--green)" stroke-width="3.5" stroke-linecap="round">
      <path d="M120,164 Q120,184 142,184 L166,184 Q176,184 176,194 L176,240"/>
      <path d="M139,106 L139,150 Q139,168 160,170 Q181,172 181,188 L181,240"/>
      <path d="M186,145 L186,240"/>
      <path d="M231,106 L231,150 Q231,168 210,170 Q191,172 191,188 L191,240"/>
      <path d="M252,163 Q252,184 230,184 L206,184 Q196,184 196,194 L196,240"/>
    </g>
    <g fill="var(--green-bright)" stroke="var(--green)" stroke-width="2">
      <circle cx="120" cy="144" r="20"/>
      <circle cx="139" cy="86" r="20"/>
      <circle cx="186" cy="125" r="20"/>
      <circle cx="231" cy="86" r="20"/>
      <circle cx="252" cy="143" r="20"/>
    </g>
    <g fill="var(--white)">
      <!-- identify: coin stack -->
      <rect x="109" y="135" width="11" height="4" rx="2"/><rect x="109" y="141" width="11" height="4" rx="2"/><rect x="109" y="147" width="11" height="4" rx="2"/>
      <circle cx="126" cy="148" r="6"/>
      <!-- acquire: bag -->
      <path d="M134,77 h10 l-2,4 q6,4 5,12 h-16 q-1,-8 5,-12z"/>
      <!-- manage: pie -->
      <path d="M186,115 A10,10 0 1 1 185.9,115 Z M186,117 L186,125 L194,125 A8,8 0 0 0 186,117Z" fill-rule="evenodd"/>
      <!-- reinvest: pot -->
      <path d="M225,77 h12 l-2,18 h-8z"/>
      <!-- divest: ring -->
      <path d="M252,131 a12,12 0 1 1 -11,8 l3,1 a9,9 0 1 0 8,-6z"/>
    </g>
    <g fill="var(--green-bright)" font-family="Poppins,sans-serif" font-weight="700" font-size="8">
      <text x="136.5" y="90">$</text><text x="228.5" y="90">$</text><text x="249.5" y="146">$</text>
    </g>
  </svg>
  <header class="section-head" style="left:10px;top:26px">
    <svg viewBox="0 0 52 36" aria-hidden="true">
      <polygon points="10,11 18,15.5 18,24.5 10,29 2,24.5 2,15.5" fill="#cfcfcf"/>
      <polygon points="20,1 25,4 25,9 20,12 15,9 15,4" fill="var(--gold)"/>
      <polygon points="34,4 48,12 48,28 34,36 20,28 20,12" fill="var(--green)"/>
    </svg>
    <h2 class="pill" style="width:318px">HOW DOES PRIVATE HOLDINGS SCHEME WORK?</h2>
  </header>
  <div class="step-label" style="left:98px;top:59px"><b>02</b><span>ACQUIRE</span></div>
  <div class="step-label" style="left:186px;top:73px"><b>03</b><span>MANAGE</span></div>
  <div class="step-label" style="left:283px;top:59px"><b>04</b><span>REINVESTMENT</span></div>
  <div class="step-label" style="left:84px;top:107px"><b>01</b><span>IDENTIFY</span></div>
  <div class="step-label" style="left:296px;top:107px"><b>05</b><span>DIVESTMENT</span></div>
  <div class="brand-name" style="left:126px;top:250px;width:120px;font-size:12px">Stonebrook<br>Minerals, LLC</div>

  <header class="section-head" style="left:10px;top:298px">
    <svg viewBox="0 0 52 36" aria-hidden="true">
      <polygon points="10,11 18,15.5 18,24.5 10,29 2,24.5 2,15.5" fill="#cfcfcf"/>
      <polygon points="20,1 25,4 25,9 20,12 15,9 15,4" fill="var(--gold)"/>
      <polygon points="34,4 48,12 48,28 34,36 20,28 20,12" fill="var(--green)"/>
    </svg>
    <h2 class="pill">WHY STONEBROOK MINERALS, LLC?</h2>
  </header>
  <div class="why-copy">
    <figure class="framed-photo">
      <div class="fill" role="img" aria-label="Photo of coin stacks on financial charts with a pen" style="background:linear-gradient(120deg,#e9edf3,#c9a24a 45%,#9aa3b0 70%,#eef1f5)"></div>
    </figure>
    <ul class="bullet-list">
      <li>• Stonebrook is a professional group who has operated successfully for over 11 years.</li>
      <li>• Stonebrook has developed a proprietary system for this asset class and has a team in place that manages the entire process for investors from A-Z.</li>
      <li>• Through the development of our various partnerships, we now have a unique system that a small group of select individuals can take advantage of in the same way as larger groups and passively own an asset coveted by many industry professionals who have acquired energy royalties for decades.</li>
    </ul>
  </div>
  <div class="footer-band" style="right:26px"></div>
  <div class="page-tab" style="right:0">3</div>
</section>

<!-- Contact page -->
<section class="page contact">
  <svg class="page-art" viewBox="0 0 372 526" aria-hidden="true">
    <defs>
      <linearGradient id="glassCoins" x1="0" y1="0" x2="1" y2="1">
        <stop offset="0" stop-color="#c9d3e6"/><stop offset=".5" stop-color="#e3dcef"/><stop offset="1" stop-color="#b9d1d6"/>
      </linearGradient>
    </defs>
    <polygon points="200,80 372,-10 420,30 420,480 330,530 120,530 40,480 40,230" fill="#ececec"/>
    <g fill="none" stroke="#e6e6e6" stroke-width="9">
      <polygon points="300,0 372,-40 440,0 440,120 372,160 300,120"/>
    </g>
    <polygon role="img" aria-label="Soft-focus photo of coin stacks in pale blue light" points="0,0 172,0 172,105 96,148 96,192 48,218 0,192" fill="url(#glassCoins)" stroke="#ececec" stroke-width="4"/>
    <polygon points="186,195 294,257 294,382 186,445 78,382 78,257" fill="var(--green)" stroke="var(--green)" stroke-width="18" stroke-linejoin="round"/>
  </svg>
  <div class="brand-name">Stonebrook<br>Minerals, LLC</div>
  <ul class="contact-list">
    <li style="font-size:15px;line-height:18px;margin-bottom:8px">
      <svg viewBox="0 0 16 16" aria-hidden="true"><path d="M4,1 L7,5 L5,7 Q7,10 9,11 L11,9 L15,12 L13,15 Q6,15 1,4Z" fill="none" stroke="#fff" stroke-width="1.4"/></svg>00 (123) 456 7890</li>
    <li style="font-size:11.5px;line-height:16px;margin-bottom:9px">
      <svg viewBox="0 0 16 16" aria-hidden="true"><rect x="1" y="3" width="14" height="10" fill="#fff"/><path d="M1,3 L8,9 L15,3" fill="none" stroke="var(--green)" stroke-width="1.2"/></svg>info@website.com</li>
    <li style="font-size:11.5px;line-height:16px;margin-bottom:9px">
      <svg viewBox="0 0 16 16" aria-hidden="true"><g fill="none" stroke="#fff" stroke-width="1.3"><circle cx="8" cy="8" r="7"/><ellipse cx="8" cy="8" rx="3" ry="7"/><path d="M1,8 H15 M2.5,4.5 H13.5 M2.5,11.5 H13.5"/></g></svg>www.website.com</li>
    <li style="font-size:11px;line-height:13px">
      <svg viewBox="0 0 16 16" aria-hidden="true"><path d="M8,1 A5,5 0 0 1 13,6 Q13,10 8,15 Q3,10 3,6 A5,5 0 0 1 8,1Z M8,4 A2,2 0 1 0 8.01,4Z" fill="#fff" fill-rule="evenodd"/></svg>Lorem ipsum dolor sit amet, consectetuer adipiscing elit</li>
  </ul>
  <div class="footer-band">www.website.com</div>
</section>

</body>
</html>
```